Financial Services Consultant needs a business card

We need a business card for a new consulting company based in Melbourne called
"Qorvel Insights". Tagline is Track, Review, Improve
We would like to see business card designs that are in line with the minimal style of the website www.qorvel-insights.example
The font I have used on the website is Proxima Nova and would like the same or similar font used on the business card with a minimal design in line with the website Two sided with "QORVEL INSIGHTS" TRACK, REVIEW, IMPROVE on one side and name, title and contact details on the otther
Updates

Hi All, thanks for your submissions, much appreciated.

I have recently added some colour to my webiste, it is hex #3a7b74 for those that wish to use it
Thanks

Hi all

thanks very much for your design submissions I am very impressed and they are much appreciated.

Interms of general feedback please find below;

Colour: I am trying to stick to a minimal design and colour scheme for my website which is still under construction, up to 3 colours( www.qorvel-insights.example) it is currently black and white with a small amount of blue/green but I am open to suggestion/interpretations for a consulting company.

Card: I dont mind if it has rounded edges or straight, I was thinking about using a letterpress card if possible

Detail: the detail on the card will include; Name, Title, Mobile, Personal Email, Business Email,Web,Business Address

Once again thanks for submissions

Industry/Entity Type

Business

```html
<!DOCTYPE html>
<html lang="en">
<head>
<meta charset="utf-8">
<title>Qorvel Insights — Business Card</title>
<link rel="stylesheet" href="https://fonts.googleapis.com/css2?family=Montserrat:wght@400;500;700&display=swap">
<style>
  :root {
    --page-bg: #2b2b2b;
    --card-stock: #e9e8e4;
    --ink: #141414;
    --card-shadow: rgba(0, 0, 0, 0.35);
  }
  * { box-sizing: border-box; margin: 0; padding: 0; }
  html, body {
    width: 1200px;
    height: 900px;
    overflow: hidden;
    background: var(--page-bg);
    font-family: "Montserrat", "Helvetica Neue", Arial, sans-serif;
    color: var(--ink);
  }
  .sheet {
    width: 1200px;
    height: 900px;
    display: flex;
    flex-direction: column;
    align-items: center;
    justify-content: center;
    gap: 40px;
  }
  .card {
    position: relative;
    width: 640px;
    height: 391px;
    background: var(--card-stock);
    box-shadow: 0 12px 30px var(--card-shadow);
  }
  /* Front face */
  .card--front {
    display: flex;
    align-items: center;
    justify-content: center;
  }
  .brand {
    text-align: left;
  }
  .brand__name {
    font-weight: 700;
    font-size: 36px;
    letter-spacing: 0.12em;
    line-height: 1;
  }
  .brand__tagline {
    margin-top: 16px;
    font-weight: 500;
    font-size: 11px;
    letter-spacing: 0.4em;
    text-transform: uppercase;
  }
  /* Back face */
  .person {
    position: absolute;
    top: 150px;
    left: 0;
    right: 0;
    text-align: center;
  }
  .person__name {
    font-weight: 700;
    font-size: 17px;
    letter-spacing: 0.22em;
    text-transform: uppercase;
  }
  .person__title {
    margin-top: 6px;
    font-weight: 400;
    font-size: 13px;
  }
  .contact {
    position: absolute;
    left: 44px;
    top: 228px;
    font-size: 13px;
    line-height: 1.6;
    list-style: none;
  }
  .address {
    position: absolute;
    right: 44px;
    top: 290px;
    font-style: normal;
    font-size: 13px;
    line-height: 1.6;
    text-align: right;
  }
</style>
</head>
<body>
  <main class="sheet">
    <section class="card card--front" aria-label="Card front">
      <div class="brand">
        <h1 class="brand__name">QORVEL INSIGHTS</h1>
        <p class="brand__tagline">Track, Review, Improve</p>
      </div>
    </section>

    <section class="card card--back" aria-label="Card back">
      <div class="person">
        <h2 class="person__name">Marcus Feldane</h2>
        <p class="person__title">Principal Consultant</p>
      </div>
      <ul class="contact">
        <li>0400 123 456</li>
        <li>marcus@qorvel-insights.example</li>
        <li>www.qorvel-insights.example</li>
      </ul>
      <address class="address">
        88 Wren Street, Fairhaven<br>
        Victoria 3999
      </address>
    </section>
  </main>
</body>
</html>
```